Music Artist Needs Flyer Design ASAP

Looking for a flyer design to promote for artist release party. Music artist is mainly hip hop based. We would like designs that are simple, creative and eye catching.

Requirements
Must have
• The flyer must have the photo of the artist I attached incorporated into the design. Must say "Free ZuRK" Release Party, Live at Toller's Bar Thursday Dec.27 2012 (artist name=ZuRK VeNT), show starts at 8pm, No cover charge, 21 and over, Register to Win Borvale Comets tickets Giveaway

```html
<!DOCTYPE html>
<html lang="en">
<head>
<meta charset="utf-8">
<title>Free ZuRK Release Party</title>
<link rel="stylesheet" href="https://fonts.googleapis.com/css2?family=Permanent+Marker&family=Ultra&family=Black+Ops+One&family=Arimo:wght@400;700&display=swap">
<style>
  :root {
    --ink: #000000;
    --paper: #ffffff;
    --neon-yellow: #f4e21c;
    --band-gold: #f7c12b;
    --photo-warm: #d89a3a;
    --photo-deep: #5a3414;
  }
  html, body { margin: 0; padding: 0; overflow: hidden; background: var(--ink); }
  .flyer {
    position: relative;
    width: 810px;
    height: 1200px;
    background: var(--ink);
    overflow: hidden;
    font-family: "Arimo", Arial, sans-serif;
  }
  .artist-photo {
    position: absolute;
    left: 58px; top: 150px;
    width: 556px; height: 692px;
    background:
      radial-gradient(ellipse at 30% 30%, #f3c88a 0%, transparent 45%),
      linear-gradient(160deg, var(--photo-warm) 0%, #b9702a 45%, var(--photo-deep) 100%);
  }
  .box {
    position: absolute;
    background: var(--ink);
    color: var(--paper);
    white-space: nowrap;
    overflow: hidden;
    text-align: center;
  }
  .headline {
    position: absolute;
    left: 40px; top: 18px;
    width: 720px; height: 130px;
    margin: 0;
    font-family: "Permanent Marker", "Comic Sans MS", cursive;
    font-weight: 400;
    font-size: 100px;
    line-height: 130px;
    text-align: center;
    white-space: nowrap;
    color: var(--neon-yellow);
    letter-spacing: 1px;
  }
  .slab { font-family: "Ultra", "Rockwell Extra Bold", Georgia, serif; font-weight: 400; }
  .tag-release { left: 268px; top: 180px; width: 470px; height: 56px; font-size: 38px; line-height: 56px; }
  .tag-live { left: 425px; top: 262px; width: 335px; height: 60px; font-size: 44px; line-height: 62px; }
  .tag-venue { left: 318px; top: 322px; width: 442px; height: 82px; font-size: 44px; line-height: 82px; }
  .tag-artist {
    left: 318px; top: 404px; width: 442px; height: 128px;
    font-family: "Black Ops One", Impact, sans-serif;
    font-size: 66px; line-height: 128px;
    color: var(--neon-yellow);
  }
  .date-column { left: 490px; top: 560px; width: 300px; height: 282px; }
  .date-column span { display: block; font-weight: 700; }
  .date-day { font-size: 48px; line-height: 60px; margin-top: 20px; }
  .date-month { font-size: 58px; line-height: 62px; }
  .date-num { font-size: 82px; line-height: 84px; }
  .date-year { font-size: 50px; line-height: 54px; }
  .showtime {
    position: absolute; left: 58px; top: 850px; width: 700px; height: 70px;
    color: var(--paper); white-space: nowrap; line-height: 70px;
  }
  .showtime .lead { font-size: 40px; }
  .showtime .time { font-family: "Arimo", Arial, sans-serif; font-size: 62px; font-weight: 700; }
  .info-band {
    position: absolute; left: 58px; top: 952px;
    width: 690px; height: 200px; background: var(--band-gold);
  }
  .cover-badge {
    position: absolute; left: 74px; top: 962px;
    width: 184px; height: 184px; border-radius: 50%;
    background: var(--ink); color: var(--paper);
    text-align: center; font-weight: 700; font-size: 38px; line-height: 42px;
    display: flex; flex-direction: column; justify-content: center;
  }
  .cover-badge .big { font-size: 46px; line-height: 46px; }
  .age-rule {
    position: absolute; left: 262px; top: 958px; width: 486px; height: 60px;
    display: flex; align-items: center; gap: 8px;
  }
  .age-rule::before, .age-rule::after {
    content: ""; height: 4px; background: var(--ink); flex: 1;
  }
  .age-rule span { font-size: 48px; font-weight: 700; color: var(--ink); white-space: nowrap; }
  .giveaway {
    position: absolute; left: 262px; top: 1032px; width: 486px;
    text-align: center; color: var(--ink); font-weight: 700; white-space: nowrap;
  }
  .giveaway span { display: block; }
  .giveaway .line1 { font-size: 32px; line-height: 38px; }
  .giveaway .line2 { font-size: 42px; line-height: 44px; }
  .giveaway .line3 { font-size: 30px; line-height: 34px; }
</style>
</head>
<body>
<div class="flyer">
  <div class="artist-photo" role="img" aria-label="Photo of the artist in a white t-shirt in front of a graffiti wall"></div>

  <h1 class="headline">Free ZuRK</h1>
  <div class="box slab tag-release">Release Party</div>
  <div class="box slab tag-live">Live at</div>
  <div class="box slab tag-venue">Toller's bar</div>
  <div class="box tag-artist">ZURK VENT</div>

  <div class="box date-column">
    <span class="date-day">Thursday</span>
    <span class="date-month">Dec</span>
    <span class="date-num">27</span>
    <span class="date-year">2012</span>
  </div>

  <div class="showtime"><span class="lead slab">Show starts at </span><span class="time">8pm</span></div>

  <div class="info-band"></div>
  <div class="cover-badge"><span class="big">NO</span><span>cover</span><span>charge</span></div>
  <div class="age-rule"><span>21 and over</span></div>
  <div class="giveaway">
    <span class="line1">Register to Win</span>
    <span class="line2">Borvale Comets</span>
    <span class="line3">tickets Giveaway</span>
  </div>
</div>
</body>
</html>
```